Concrete Construction Business Card design

We are a commercial concrete construction company based in Texas. a family owned business which our trade was passed down and taught by our grandfather whom we want represented in this design. our grandfathers nick name was "paprika" so we are wanting the letter G to be symbolized in some way with a red paprika . colors should be possibly a grey color back ground , green letter g and red paprika pepper , to be left for you to decide with integrity , concrete professionalism,and mexican heritage

Target Market(s)

general contractors, architects,inverstors, and engineers

Industry/Entity Type

Concrete

Contact Information for Business Card

Varela Concrete Construction LLC, Dwight Varela, 1718 Briarcliff Dr. Denton, TX 76209, (940)412-3759, dvslabworks58@mailbrook.net

```html
<!DOCTYPE html>
<html lang="en">
<head>
<meta charset="utf-8">
<title>Varela Concrete Construction LLC – Business Card</title>
<link rel="stylesheet" href="https://fonts.googleapis.com/css2?family=Play:wght@400;700&family=Tinos&display=swap">
<style>
  :root {
    --page-bg: #e6e4e1;
    --card-grey: #505050;
    --card-grey-light: #5c5c5c;
    --brand-green: #3a9a3c;
    --paprika-red: #c8232a;
    --name-grey: #b9b9b9;
    --text-light: #e4e4e4;
  }
  * { margin: 0; padding: 0; box-sizing: border-box; }
  html, body {
    width: 1200px;
    height: 900px;
    overflow: hidden;
    background: var(--page-bg);
  }
  .card {
    position: absolute;
    left: 110px;
    top: 170px;
    width: 980px;
    height: 560px;
    background: linear-gradient(135deg, var(--card-grey-light), var(--card-grey));
    overflow: hidden;
    box-shadow: 0 10px 30px rgba(0,0,0,0.25);
  }
  .brand {
    position: absolute;
    left: 260px;
    top: 70px;
    display: flex;
    align-items: center;
    gap: 18px;
  }
  .brand-mark {
    width: 26px;
    height: 26px;
    background: var(--brand-green);
  }
  .brand-name {
    font-family: "Tinos", serif;
    font-size: 30px;
    line-height: 1.1;
    color: var(--text-light);
  }
  .person-name {
    position: absolute;
    left: 300px;
    top: 180px;
    font-family: "Play", sans-serif;
    font-weight: 700;
    font-size: 50px;
    color: var(--name-grey);
  }
  .accent-band {
    position: absolute;
    left: 560px;
    right: 0;
    top: 230px;
    height: 110px;
    background: var(--brand-green);
  }
  .accent-block {
    position: absolute;
    left: 45px;
    bottom: 0;
    width: 55px;
    height: 120px;
    background: var(--brand-green);
  }
  .contact-list {
    position: absolute;
    left: 135px;
    top: 420px;
    list-style: none;
    font-family: "Play", sans-serif;
    font-weight: 700;
    font-size: 24px;
    color: var(--text-light);
  }
  .contact-list li {
    display: flex;
    align-items: center;
    gap: 14px;
    height: 36px;
  }
  .contact-icon {
    width: 16px;
    height: 16px;
    flex: none;
  }
</style>
</head>
<body>
  <main class="card">
    <div class="brand">
      <span class="brand-mark"></span>
      <span class="brand-name">Varela Concrete<br>Construction LLC</span>
    </div>

    <h1 class="person-name">Dwight Varela</h1>

    <div class="accent-band"></div>
    <div class="accent-block"></div>

    <ul class="contact-list">
      <li>
        <svg class="contact-icon" viewBox="0 0 16 16" aria-hidden="true">
          <path fill="var(--paprika-red)" d="M3 1h3l1 4-2 1.5a9 9 0 0 0 4.5 4.5L11 9l4 1v3a2 2 0 0 1-2 2A12 12 0 0 1 1 3a2 2 0 0 1 2-2z"/>
        </svg>
        (940)412-3759
      </li>
      <li>
        <svg class="contact-icon" viewBox="0 0 16 16" aria-hidden="true">
          <rect x="1" y="3" width="14" height="10" rx="1" fill="var(--paprika-red)"/>
          <path d="M1.5 4 8 9l6.5-5" fill="none" stroke="var(--card-grey)" stroke-width="1.4"/>
        </svg>
        dvslabworks58@mailbrook.net
      </li>
      <li>
        <svg class="contact-icon" viewBox="0 0 16 16" aria-hidden="true">
          <path fill="var(--paprika-red)" d="M8 0a5.5 5.5 0 0 0-5.5 5.5C2.5 10 8 16 8 16s5.5-6 5.5-10.5A5.5 5.5 0 0 0 8 0zm0 7.5a2 2 0 1 1 0-4 2 2 0 0 1 0 4z"/>
        </svg>
        1718 Briarcliff Dr. Denton, TX 76209
      </li>
    </ul>
  </main>
</body>
</html>
```